Online religious stickers company needs a letterhead design

I need a letterhead design for a startup internet company that sells religious stickers and magnets. I would like to see a design that incorporates the color blue any shade of blue is fine. Maybe the use of very light clouds signifying heaven but it is not necessary. I am attaching my logo the color can be changed if necessary.
I do not want something that is very busy. Simple is better.

Religious

```html
<!DOCTYPE html>
<html lang="en">
<head>
<meta charset="utf-8">
<title>Halo Mark Letterhead</title>
<link rel="stylesheet" href="https://fonts.googleapis.com/css2?family=Questrial&display=swap">
<style>
  :root {
    --band-blue: #c5e7f8;
    --cloud-blue: #dff1fb;
    --paper: #ffffff;
    --ink: #111111;
  }
  * { margin: 0; padding: 0; box-sizing: border-box; }
  html, body {
    width: 847px;
    height: 1200px;
    overflow: hidden;
    background: var(--paper);
  }
  .letterhead {
    position: relative;
    width: 847px;
    height: 1200px;
    background: var(--paper);
    font-family: "Questrial", "Century Gothic", sans-serif;
    color: var(--ink);
  }
  .header-band {
    position: absolute;
    top: 0; left: 0;
    width: 100%;
    height: 142px;
    background: var(--band-blue);
  }
  .brand {
    position: absolute;
    left: 80px;
    top: 46px;
    display: flex;
    align-items: center;
    gap: 14px;
  }
  .brand-dot {
    width: 40px;
    height: 40px;
    border-radius: 50%;
    background: var(--ink);
  }
  .brand-name {
    font-size: 38px;
    letter-spacing: 1px;
    color: var(--ink);
    line-height: 1;
  }
  .cloud-area {
    position: absolute;
    left: 0;
    top: 820px;
    width: 100%;
    height: 230px;
    background: linear-gradient(to bottom, rgba(223, 241, 251, 0) 0%, var(--cloud-blue) 45%, var(--cloud-blue) 100%);
  }
  .footer-band {
    position: absolute;
    left: 0;
    top: 1058px;
    width: 100%;
    height: 142px;
    background: var(--band-blue);
  }
  .contact {
    position: absolute;
    font-size: 16px;
    line-height: 22px;
    color: var(--ink);
  }
  .contact-direct {
    left: 64px;
    top: 1094px;
  }
  .contact-address {
    right: 61px;
    top: 1116px;
    text-align: right;
  }
</style>
</head>
<body>
  <div class="letterhead">
    <header class="header-band">
      <div class="brand">
        <span class="brand-dot"></span>
        <span class="brand-name">Halo Mark</span>
      </div>
    </header>

    <div class="cloud-area" role="img" aria-label="Soft light blue clouds rising along the lower edge of the page"></div>

    <footer class="footer-band"></footer>
    <div class="contact contact-direct">
      <p>M: 055501234</p>
      <p>T: 055501234</p>
      <p>E: hello@halomark.com</p>
    </div>
    <div class="contact contact-address">
      <p>00412 Fairview, USA</p>
      <p>www.halomark.com</p>
    </div>
  </div>
</body>
</html>
```